Create a bold and border around my logo to make it pop and sign graphic design

I would like someone to create a sign graphic design so I can use on the side of my trucks and put on yard signs. I would to remove a lot of the white and add more of the orange and blue to give it more pop when cars drive past. I would like the services to be removed and for you to leave space for a mobile number that i would add later. I don’t want my logo changed at all. I just want colour and design to be added to the background so i can use it in signage. Same colour as on the sign

```html
<!DOCTYPE html>
<html lang="en">
<head>
<meta charset="utf-8">
<title>Oakworthy – Truck &amp; Yard Sign</title>
<link rel="stylesheet" href="https://fonts.googleapis.com/css2?family=Montserrat:wght@500;600&display=swap">
<style>
  :root {
    --orange: #e2450a;
    --orange-deep: #d93400;
    --orange-light: #ea5a12;
    --navy: #062a6b;
    --navy-deep: #041f56;
    --white: #ffffff;
    --backdrop: #eef0f3;
  }

  * { margin: 0; padding: 0; box-sizing: border-box; }

  html, body {
    width: 1200px;
    height: 950px;
    overflow: hidden;
    background: var(--backdrop);
  }

  .canvas {
    position: relative;
    width: 1200px;
    height: 950px;
    display: flex;
    align-items: center;
    justify-content: center;
  }

  .sign {
    position: relative;
    width: 1120px;
    height: 620px;
    overflow: hidden;
    box-shadow: 0 10px 30px rgba(0, 0, 0, 0.12);
  }

  .band-orange {
    position: absolute;
    left: 0; top: 0;
    width: 100%;
    height: 298px;
    background: linear-gradient(120deg, var(--orange-light) 0%, var(--orange-deep) 45%, var(--orange) 75%, var(--orange-light) 100%);
  }

  .band-white {
    position: absolute;
    left: 0; top: 298px;
    width: 100%;
    height: 148px;
    background: var(--white);
  }

  .band-navy {
    position: absolute;
    left: 0; top: 446px;
    width: 100%;
    height: 174px;
    background: linear-gradient(120deg, var(--navy) 0%, var(--navy-deep) 55%, var(--navy) 100%);
  }

  .badge-circle {
    position: absolute;
    left: 278px;
    top: 10px;
    width: 300px;
    height: 300px;
    border-radius: 50%;
    background: var(--white);
  }

  .brand-name {
    position: absolute;
    left: 0;
    top: 298px;
    width: 100%;
    height: 148px;
    display: flex;
    align-items: center;
    justify-content: center;
    padding-left: 40px;
    font-family: "Montserrat", sans-serif;
    font-weight: 600;
    font-size: 104px;
    letter-spacing: 2px;
    color: var(--navy);
    line-height: 1;
    white-space: nowrap;
  }

  .phone {
    position: absolute;
    left: 0;
    top: 446px;
    width: 100%;
    height: 174px;
    display: flex;
    align-items: center;
    justify-content: center;
    gap: 14px;
    padding-left: 20px;
    font-family: "Montserrat", sans-serif;
    font-weight: 500;
    font-size: 118px;
    color: var(--white);
    line-height: 1;
    white-space: nowrap;
  }

  .phone-icon {
    width: 68px;
    height: 100px;
    flex: none;
  }
</style>
</head>
<body>
  <main class="canvas">
    <section class="sign" aria-label="Oakworthy sign">
      <div class="band-orange"></div>
      <div class="band-white"></div>
      <div class="band-navy"></div>

      <div class="badge-circle"></div>

      <h1 class="brand-name">OAKWORTHY</h1>

      <p class="phone">
        <svg class="phone-icon" viewBox="0 0 68 100" aria-hidden="true">
          <path fill="var(--white)" d="M14 4 C8 6 4 12 4 22 C4 48 18 78 40 94 C46 98 54 98 60 93 L64 89 C66 87 66 84 64 82 L52 68 C50 66 47 66 45 68 L40 72 C30 62 24 48 22 36 L28 33 C31 32 32 29 31 26 L26 8 C25 5 22 3 19 3 Z"/>
        </svg>
        <span class="phone-number">0487215936</span>
      </p>
    </section>
  </main>
</body>
</html>
```